Solar Company Bussiness Card

I need a 2 sided business card and would like a .psd and any font files for each side of the card. I would like my logo used, it should be attached with the fonts. I'm not opposed to the font colors with the logo being changed.

On the sample design, I'd like the following:

Warren Kettle
President
Phone: 570-318-4957
www.brightvalepower.example

As I've recently opened in a 2nd market, I'm not sure about an address as I currently have 2 of them. I may actually get separate cards printed, one batch for each address, that's why I need the PSD file.
Updates

I'm very pleased with the response and designs I've received here for my business card. First and foremost, I'd like to thank everyone who took the time to submit a design. There truly are a lot of great designs in the bunch here and I'm having a little difficulty deciding. I will be reaching out to someone in the next day or two here to go to a final design. At this time, I'm not looking for any new concepts. If any of you do logos, I'm looking for a new logo for our sister entity, Kettle Partners, Inc. Thanks, Warren Kettle

Reason: I'm not looking for any new designs at this point, but extending this deadline in order to give people I've asked a chance to re-submit items.

```html
<!DOCTYPE html>
<html lang="en">
<head>
<meta charset="utf-8">
<title>Brightvale Power – Business Card</title>
<link href="https://fonts.googleapis.com/css2?family=Open+Sans:wght@400;600;700&display=swap" rel="stylesheet">
<style>
  :root {
    --bg: #8a8a8a;
    --card: #ffffff;
    --navy: #1a4f8f;
    --blue: #1f6cc0;
    --blue-light: #4a9be0;
    --ink: #1e4f8a;
    --dot: #15487f;
  }
  * { margin: 0; padding: 0; box-sizing: border-box; }
  html, body { width: 1200px; height: 894px; overflow: hidden; }
  body {
    background: var(--bg);
    font-family: "Open Sans", Arial, sans-serif;
    display: flex;
    flex-direction: column;
    align-items: center;
    justify-content: center;
    gap: 56px;
  }
  .card {
    position: relative;
    width: 620px;
    height: 354px;
    background: var(--card);
    overflow: hidden;
  }
  .card__edges { position: absolute; inset: 0; width: 100%; height: 100%; }

  /* front */
  .holder { position: absolute; left: 62px; top: 52px; color: var(--blue); }
  .holder__name { font-weight: 700; font-size: 22px; letter-spacing: .5px; }
  .holder__title { font-weight: 400; font-size: 18px; letter-spacing: .5px; margin-top: 2px; }

  .contact { position: absolute; left: 96px; top: 146px; width: 240px; color: var(--ink); font-size: 13.5px; line-height: 21px; }
  .contact__line { display: flex; justify-content: flex-end; align-items: center; gap: 8px; }
  .contact__dot { width: 14px; height: 14px; border-radius: 50%; background: var(--dot); flex: none; }
  .contact__gap { width: 14px; flex: none; }

  .brand { position: absolute; display: flex; align-items: center; gap: 12px; color: var(--navy); font-weight: 600; }
  .brand__mark { width: 34px; height: 34px; background: var(--blue); flex: none; }
  .brand__name { font-size: 34px; line-height: 1; letter-spacing: .3px; }
  .brand__sub { display: block; font-size: 15px; letter-spacing: 3px; text-align: right; margin-top: 4px; }
  .card--front .brand { right: 70px; top: 200px; }

  /* back */
  .card--back .brand { left: 50%; top: 120px; transform: translateX(-50%); }
  .back__url { position: absolute; left: 0; right: 0; top: 236px; text-align: center; color: #333; font-size: 17px; letter-spacing: .5px; }
</style>
</head>
<body>

  <section class="card card--front" aria-label="Card front">
    <svg class="card__edges" viewBox="0 0 620 354" aria-hidden="true">
      <defs>
        <linearGradient id="edgeGrad" x1="0" y1="0" x2="0" y2="1">
          <stop offset="0" stop-color="#1f6cc0"/>
          <stop offset=".5" stop-color="#4a9be0"/>
          <stop offset="1" stop-color="#1f6cc0"/>
        </linearGradient>
      </defs>
      <polygon points="0,0 16,24 16,330 0,354" fill="url(#edgeGrad)"/>
      <polygon points="620,0 604,24 604,330 620,354" fill="url(#edgeGrad)"/>
    </svg>

    <div class="holder">
      <div class="holder__name">WARREN KETTLE</div>
      <div class="holder__title">PRESIDENT</div>
    </div>

    <div class="contact">
      <div class="contact__line"><span>Kettle Ave. 210B</span><span class="contact__gap"></span></div>
      <div class="contact__line"><span>Hillcrest, Ontario</span><span class="contact__gap"></span></div>
      <div class="contact__line"><span>570-318-4957</span><span class="contact__dot"></span></div>
      <div class="contact__line"><span>570-318-4957</span><span class="contact__dot"></span></div>
      <div class="contact__line"><span>info@brightvalepower.example</span><span class="contact__dot"></span></div>
      <div class="contact__line"><span>www.brightvalepower.example</span><span class="contact__dot"></span></div>
    </div>

    <div class="brand">
      <span class="brand__mark"></span>
      <span class="brand__name">Brightvale<span class="brand__sub">POWER</span></span>
    </div>
  </section>

  <section class="card card--back" aria-label="Card back">
    <svg class="card__edges" viewBox="0 0 620 354" aria-hidden="true">
      <polygon points="0,0 16,24 16,330 0,354" fill="url(#edgeGrad)"/>
      <polygon points="620,0 604,24 604,330 620,354" fill="url(#edgeGrad)"/>
    </svg>

    <div class="brand">
      <span class="brand__mark"></span>
      <span class="brand__name">Brightvale<span class="brand__sub">POWER</span></span>
    </div>
    <div class="back__url">www.brightvalepower.example</div>
  </section>

</body>
</html>
```